Fitness Centre/Personal Trainer Business Card

We need a business card design for a company based in Singapore called 'Vigor Summit'.

We are a team of Personal Trainers and we are planning to open our new training facility.

This design will also be printed/painted on the walls in our gym.

We are a new breed of personal trainers who take fitness seriously and holistically. We do not merely train our clients to be big and muscular.

We believe in wholeness. In our opinion, fitness should include: strength, speed, flexibility, mobility, stamina & agility. These are what we train for. Of course, nutrition/diet is key.

We use fitness tools such as kettlebells, QLV, Pylometric boxes, battling ropes, clubbells, medicine balls, bulgarian bags etc - functional and non-bulky tools.

I currently have a Facebook page 'Vigor Summit SG' which shows a logo of a kettlebell. But my business focus has since changed.

Services provided:
- Kettlebell Sport Preparation
- Calisthenics Training
- Corrective Exercises
- Sports Strength & Conditioning
- 28 days Weight Loss Program
- Myofascial Rehab Therapy
- Sports/Thai Massage

Main colors for the design should be BLACK & YELLOW. We envision a design which is able to protray the holistic view we take on fitness. Also it should somewhat appeal to the ladies and not intimidate them.

Target Market(s)

People between 18-35 years old. Students and working class alike.

Industry/Entity Type

Training

Requirements
Must have
• Name: Marcus Oleander Pryce
Fitness Coach
Corrective Exercise Specialist
M: +65 9372 6058
E: marcus@sgvigorsummit-example.com

Double-sided please.
Nice to have
• "What is your vigor summit?"

```html
<!DOCTYPE html>
<html lang="en">
<head>
<meta charset="utf-8">
<title>Vigor Summit – Business Card</title>
<link rel="stylesheet" href="https://fonts.googleapis.com/css2?family=PT+Sans:wght@400;700&display=swap">
<style>
  :root {
    --black: #050505;
    --charcoal: #2a2a2a;
    --yellow: #ffe100;
    --white: #ffffff;
    --photo-light: #f2f2f2;
    --photo-mid: #c9c9cc;
    --backdrop: #e7e4df;
  }
  * { margin: 0; padding: 0; box-sizing: border-box; }
  html, body { width: 1200px; height: 1000px; overflow: hidden; }
  body {
    background: var(--backdrop);
    font-family: "PT Sans", Arial, sans-serif;
    display: flex;
    flex-direction: column;
    align-items: center;
    justify-content: center;
    gap: 30px;
  }
  .card {
    position: relative;
    width: 760px;
    height: 457px;
    overflow: hidden;
    box-shadow: 0 8px 24px rgba(0,0,0,0.25);
  }

  /* Front */
  .card--front { background: radial-gradient(ellipse at 30% 40%, #1e1e1e 0%, var(--black) 70%); }
  .front-art { position: absolute; inset: 0; }
  .services {
    position: absolute;
    left: 50px;
    top: 46px;
    list-style: none;
    color: var(--yellow);
    font-weight: 700;
    font-size: 14px;
    line-height: 39px;
  }
  .tagline {
    position: absolute;
    left: 56px;
    top: 330px;
    font-size: 28px;
    line-height: 36px;
    color: var(--yellow);
  }
  .tagline__second { display: block; padding-left: 72px; color: var(--white); }
  .tagline__accent { color: var(--yellow); }
  .name-bar {
    position: absolute;
    left: 346px;
    top: 353px;
    width: 389px;
    height: 62px;
    background: var(--black);
    text-align: right;
    padding: 8px 36px 0 0;
  }
  .name-bar::after {
    content: "";
    position: absolute;
    right: 0;
    top: -2px;
    width: 18px;
    height: 66px;
    background: var(--yellow);
  }
  .name-bar__name { font-size: 24px; font-weight: 700; color: var(--white); line-height: 28px; }
  .name-bar__first { color: var(--yellow); }
  .name-bar__role { font-size: 14px; font-weight: 700; color: var(--yellow); line-height: 18px; }

  /* Back */
  .card--back { background: radial-gradient(ellipse at 50% 40%, #2b2b2b 0%, #121212 55%, var(--black) 100%); }
  .back-name {
    position: absolute;
    top: 170px;
    width: 100%;
    text-align: center;
    font-weight: 700;
    font-size: 40px;
    line-height: 44px;
    color: var(--white);
  }
  .back-name__first { color: var(--yellow); }
  .back-role {
    position: absolute;
    top: 222px;
    width: 100%;
    text-align: center;
    font-weight: 700;
    font-size: 24px;
    color: var(--yellow);
  }
  .contact-bar {
    position: absolute;
    left: 22px;
    right: 19px;
    top: 349px;
    height: 65px;
    background: var(--black);
    padding: 6px 0 0 34px;
  }
  .contact-bar::before, .contact-bar::after {
    content: "";
    position: absolute;
    top: 0;
    width: 18px;
    height: 65px;
    background: var(--yellow);
  }
  .contact-bar::before { left: 0; }
  .contact-bar::after { right: 0; }
  .contact-bar__title { font-size: 21px; font-weight: 700; color: var(--yellow); line-height: 28px; }
  .contact-bar__details { font-size: 16px; font-weight: 700; color: var(--white); line-height: 24px; }
  .contact-bar__label { color: var(--yellow); }
  .contact-bar__sep { color: var(--white); padding: 0 14px; }
</style>
</head>
<body>

  <section class="card card--front">
    <svg class="front-art" width="760" height="457" viewBox="0 0 760 457" role="img" aria-label="Photo of a smiling fitness trainer holding a kettlebell on her shoulder">
      <defs>
        <radialGradient id="photoTone" cx="0.75" cy="0.35" r="0.8">
          <stop offset="0" stop-color="var(--photo-light)"/>
          <stop offset="1" stop-color="var(--photo-mid)"/>
        </radialGradient>
      </defs>
      <circle cx="868" cy="225" r="572" fill="var(--yellow)"/>
      <circle cx="884" cy="225" r="562" fill="var(--black)"/>
      <circle cx="888" cy="225" r="556" fill="url(#photoTone)"/>
    </svg>

    <ul class="services">
      <li>- Kettlebell Sport Preparation</li>
      <li>- Calisthenics Training</li>
      <li>- Corrective Exercises</li>
      <li>- Sports Strength &amp; Conditioning</li>
      <li>- 28 days Weight Loss Program</li>
      <li>- Myofascial Rehab Therapy</li>
      <li>- Sports/Thai Massage</li>
    </ul>

    <p class="tagline">What is your
      <span class="tagline__second">Vigor <span class="tagline__accent">Summit?</span></span>
    </p>

    <div class="name-bar">
      <div class="name-bar__name"><span class="name-bar__first">Marcus</span> Oleander Pryce</div>
      <div class="name-bar__role">Fitness Coach</div>
    </div>
  </section>

  <section class="card card--back">
    <h1 class="back-name"><span class="back-name__first">MARCUS</span> OLEANDER PRYCE</h1>
    <p class="back-role">FITNESS COACH</p>
    <div class="contact-bar">
      <div class="contact-bar__title">Corrective Exercise Specialist</div>
      <div class="contact-bar__details">
        <span class="contact-bar__label">M:</span> +65 9372 6058<span class="contact-bar__sep">|</span><span class="contact-bar__label">E:</span> marcus@sgvigorsummit-example.com
      </div>
    </div>
  </section>

</body>
</html>
```